Keen Compass - Web Design Project

We need a website for our new company based in Sao Paulo - Brazil. Our initial product is Keen Compass - an online assessment system based on the most recent neuroscience academic research. The system gathers tests that are applied in the selection and evaluation of employees. We would like to see designs that use the colors black and blue. The final design should communicate trust. We like clean and simple designs.

Login to www.keencompass-example.com.br
login: user
pass: user

We need three pages:
1- Login page: http://www.keencompass-example.com.br/

2- Welcome page: http://www.keencompass-example.com.br/sys/admin/index.php

3- Results page: http://www.keencompass-example.com.br/sys/admin/admin_provas_resultados.php?unique_id=5

Our logo was created using ArtLoomly.
Next projetcs: Tests interface redesign.

Industry/Entity Type

It Company

Requirements
Must have
• Link folders. i.e.:
Home :: Users :: John Doe :: Test1
Nice to have
• Image Buttons
Should not have
• Noise

```html
<!DOCTYPE html>
<html lang="pt-BR">
<head>
<meta charset="utf-8">
<title>Keen Compass — Home</title>
<link rel="stylesheet" href="https://fonts.googleapis.com/css2?family=Barlow+Condensed:wght@500;600&display=swap">
<style>
  :root {
    --brand-blue: #1f6db5;
    --nav-blue: #1d68b0;
    --ink: #000000;
    --white: #ffffff;
    --header-fade: #dcdcdc;
    --rule: #c9c9c9;
    --band-dark: #000000;
    --band-dark-end: #1f1f1f;
    --art-soft: #4c8ccb;
    --art-deep: #16324f;
  }
  * { margin: 0; padding: 0; box-sizing: border-box; }
  html, body {
    width: 1200px;
    height: 597px;
    overflow: hidden;
    background: var(--white);
  }
  .page {
    position: relative;
    width: 1200px;
    height: 597px;
    font-family: Arial, Helvetica, sans-serif;
  }

  /* Header */
  .site-header {
    position: absolute;
    top: 0; left: 0;
    width: 1200px;
    height: 110px;
    border-top: 1px solid var(--rule);
    background: linear-gradient(to bottom, var(--white) 0%, var(--white) 58%, var(--header-fade) 100%);
    z-index: 2;
  }
  .header-shadow {
    position: absolute;
    top: 104px;
    left: 210px;
    width: 810px;
    height: 10px;
    border-radius: 50%;
    box-shadow: 0 6px 10px rgba(0,0,0,0.45);
    z-index: 1;
  }
  .brand {
    position: absolute;
    left: 221px;
    top: 56px;
    display: flex;
    align-items: center;
    gap: 8px;
    font-family: "Barlow Condensed", sans-serif;
    font-weight: 600;
    font-size: 32px;
    line-height: 1;
    color: var(--nav-blue);
    text-decoration: none;
  }
  .brand-dot {
    width: 14px;
    height: 14px;
    border-radius: 50%;
    background: var(--ink);
  }
  .main-nav {
    position: absolute;
    left: 518px;
    top: 65px;
    display: flex;
    gap: 27px;
    list-style: none;
  }
  .main-nav a {
    font-family: "Barlow Condensed", sans-serif;
    font-weight: 600;
    font-size: 22px;
    line-height: 1;
    color: var(--nav-blue);
    text-decoration: none;
  }
  .main-nav a.is-current { color: var(--ink); }

  /* Hero */
  .hero {
    position: absolute;
    top: 110px; left: 0;
    width: 1200px;
    height: 331px;
    background: var(--brand-blue);
  }
  .hero-title {
    position: absolute;
    left: 217px;
    top: 42px;
    width: 390px;
    z-index: 2;
    font-family: "Barlow Condensed", sans-serif;
    font-weight: 600;
    font-size: 70px;
    line-height: 80px;
    text-transform: uppercase;
    white-space: nowrap;
  }
  .hero-title .line-light { display: block; color: var(--white); text-shadow: 1px 2px 0 rgba(0,0,0,0.35); }
  .hero-title .line-dark { display: block; color: var(--ink); text-shadow: 1px 2px 0 rgba(255,255,255,0.2); }
  .hero-intro {
    position: absolute;
    left: 219px;
    top: 217px;
    width: 372px;
    font-size: 10.5px;
    line-height: 19px;
    color: var(--white);
  }
  .hero-art {
    position: absolute;
    left: 623px;
    top: 4px;
    width: 364px;
    height: 327px;
    background: linear-gradient(135deg, var(--art-soft) 0%, var(--brand-blue) 45%, var(--art-deep) 100%);
  }

  /* Dark band */
  .feature-band {
    position: absolute;
    top: 441px; left: 0;
    width: 1200px;
    height: 113px;
    background: linear-gradient(to bottom, var(--band-dark) 0%, var(--band-dark) 45%, var(--band-dark-end) 100%);
  }

  /* Footer */
  .site-footer {
    position: absolute;
    top: 554px; left: 0;
    width: 1200px;
    height: 43px;
    border-top: 1px solid var(--rule);
    text-align: center;
    padding-top: 15px;
    font-size: 10.5px;
    font-weight: bold;
    color: var(--ink);
  }
</style>
</head>
<body>
<div class="page">
  <header class="site-header">
    <a class="brand" href="#"><span class="brand-dot"></span>Keen Compass</a>
    <nav>
      <ul class="main-nav">
        <li><a class="is-current" href="#">HOME</a></li>
        <li><a href="#">PROVAS</a></li>
        <li><a href="#">USUÁRIOS</a></li>
        <li><a href="#">CONFIGURAÇÕES</a></li>
        <li><a href="#">LOGOUT</a></li>
      </ul>
    </nav>
  </header>
  <div class="header-shadow"></div>

  <section class="hero">
    <div class="hero-art" role="img" aria-label="Illustration of a head silhouette in profile surrounded by white gears, with one red gear inside the head"></div>
    <h1 class="hero-title">
      <span class="line-light">Bem-vindo ao</span>
      <span class="line-dark">Keen Compass</span>
    </h1>
    <p class="hero-intro">Lorem ipsum dolor sit amet, consectetuer adipiscing elit, sed diam nonummy nibh euismod tincidunt ut laoreet dolore magna aliquam erat volutpat. Ut wisi enim ad minim veniam, quis nostrud exerci tation ullamcorper suscipit lobortis nisl ut aliquip ex ea commodo consequat.</p>
  </section>

  <section class="feature-band"></section>

  <footer class="site-footer">© Copyrights 2013 Keen Compass. All rights reserved</footer>
</div>
</body>
</html>
```